Funky Modern Flyer A5 or Postcard size

Hi, I am looking at a one small flyer (A5 or postcard size) that I can put both on my website on the front page (ie so png) and also send out if necessary.

It has to be modern, funky and hip. My brand is professional / Corporate so it also has to fit in with that brand.

There are 6 attachments:
Example 1 - FernaPeak - I like this look, clean, modern, funky and says it all.
Example 2 - FernPeak - again another look I like, simple, explanatory
Example 4 - Brightstall Bazaar - font is cool on this one but background not so much too much going on but I like the font
Example 5 - Example 4 - Brightstall Bazaar - font is cool on this one but background not so much too much going on but I like the font
5 is my logo
Example 6 is something I found on the web this morning which is effective.

It is for a Mentoring and Training program I run called: HIGHSTRIDE

What is to be included is the following:
The name: Highstride
Somewhere: Training, Mentoring
My Logo (see attached two options) you can choose which colour suits and I have the source file should you need it
My website and email: www.miriambaskell.example / miriam@miriambaskell.example

This wording: This is one of our highest in-demand programs and is based on a background and proven track record by Miriam in accelerating sales organisations and their people into stand out high performers. **(NOTE this wording in this paragraph may change and I am open to you changing if you think you can make it more effective!)

Colours: white, black and gold (those are our website colours).

I'd like the Highstride to really stand out.... I have included two fonts that I really like that I got off Brightstall Bazaar. However, feel free to suggest other fonts that you think cool or funky!
Updates

Hi everyone, just to add a note to the brief, I am not overly keen on pictures that are really busy. I only like a picture that is minimal and effective. The examples from Brightstall Bazaar was more for the Font Style not so much the pictures in the background. The pictures can take away from a design unless done really minimally.....hope this makes sense. Miriam Added Wednesday, March 15, 2017

Target Market(s)

My target Market is Corporates but I want a Funky Modern look as a lot of people in Corporates are Millennials as well which is part of my target market

Industry/Entity Type

Information Technology

Requirements
Must have
• What is to be included is the following:
• The name: Highstride
• Somewhere: Training, Mentoring
• My Logo (see attached two options) you can choose which colour suits and I have the source file should you need it
• My website and email: www.miriambaskell.example / miriam@miriambaskell.example
• This wording: This is one of our highest in-demand programs and is based on a background and proven track record in high performance and accelerating sales organisations and their people into stand out high performers. (**NOTE this wording may change when final design is picked to be changed as still working in it***)
• Colours: white, black and gold (those are our website colours).
• I'd like the Highstride to really stand out.... I have included two fonts that I really like that I got off Brightstall Bazaar. However, feel free to suggest other fonts that you think cool or funky! NOTE: The pictures I have attached is mainly for the FONTS not for the background pictures. I am not that keen on background pictures as it can take away from the font - unless it is minimal
Should not have
• Too many different colours, I like slick, modern, clean. White, gold and black preferred as this is our website colour.
• NOTE: The pictures from Brightstall Bazaar I have attached are mainly for the FONTS not for the background pictures. I am not hugely keen on background pictures as it can take away from the font/message - unless the pictures are minimal but effective.

```html
<!DOCTYPE html>
<html lang="en">
<head>
<meta charset="utf-8">
<title>Highstride – Training, Mentoring</title>
<link rel="stylesheet" href="https://fonts.googleapis.com/css2?family=Kaushan+Script&family=Didact+Gothic&family=Questrial&display=swap">
<style>
  :root {
    --backdrop: #595959;
    --paper: #ffffff;
    --ink: #3d3d3d;
    --ink-strong: #1a1a1a;
    --gold: #e0a92a;
  }
  * { margin: 0; padding: 0; box-sizing: border-box; }
  html, body {
    width: 1200px;
    height: 1200px;
    overflow: hidden;
    background: var(--backdrop);
  }
  .flyer {
    position: absolute;
    left: 114px;
    top: 257px;
    width: 973px;
    height: 686px;
    background: var(--paper);
    color: var(--ink);
    font-family: "Didact Gothic", "Century Gothic", sans-serif;
  }
  .brand-name {
    position: absolute;
    top: 130px;
    left: 0;
    width: 100%;
    text-align: center;
    font-family: "Questrial", sans-serif;
    font-size: 29px;
    letter-spacing: 2px;
    color: var(--ink);
  }
  .program-title {
    position: absolute;
    top: 205px;
    left: 0;
    width: 100%;
    text-align: center;
    font-family: "Kaushan Script", cursive;
    font-size: 150px;
    line-height: 1.2;
    color: var(--ink);
  }
  .title-swash {
    position: absolute;
    left: 0;
    top: 0;
    width: 973px;
    height: 686px;
    pointer-events: none;
  }
  .services {
    position: absolute;
    top: 484px;
    left: 0;
    width: 100%;
    text-align: center;
    font-family: "Questrial", sans-serif;
    font-size: 29px;
    color: var(--gold);
  }
  .services-rule {
    position: absolute;
    top: 527px;
    left: 59px;
    width: 855px;
    height: 1px;
    background: var(--gold);
  }
  .program-summary {
    position: absolute;
    top: 543px;
    left: 0;
    width: 100%;
    text-align: center;
    font-size: 17px;
    line-height: 22px;
    color: var(--ink-strong);
  }
  .contact-bar {
    position: absolute;
    top: 638px;
    left: 0;
    width: 100%;
    height: 36px;
  }
  .contact-item {
    position: absolute;
    top: 5px;
    display: flex;
    align-items: center;
    gap: 9px;
    font-size: 18px;
    color: var(--ink-strong);
  }
  .contact-item--web { left: 209px; }
  .contact-item--mail { left: 510px; }
  .contact-icon { width: 26px; height: 26px; flex: none; }
  .contact-divider {
    position: absolute;
    left: 477px;
    top: 0;
    width: 1px;
    height: 34px;
    background: #9a9a9a;
  }
</style>
</head>
<body>
  <main class="flyer">
    <p class="brand-name">MIRIAM BASKELL</p>

    <h1 class="program-title">Highstride</h1>
    <svg class="title-swash" viewBox="0 0 973 686" aria-hidden="true">
      <path d="M119 403 Q230 368 362 371" fill="none" stroke="var(--ink)" stroke-width="4" stroke-linecap="round"/>
    </svg>

    <h2 class="services">Training, Mentoring</h2>
    <div class="services-rule"></div>

    <p class="program-summary">
      This is one of our highest in-demand programs and is based on<br>
      a background and proven track record in high performance and accelerating sales<br>
      organisations and their people into stand out high performers.
    </p>

    <div class="contact-bar">
      <span class="contact-item contact-item--web">
        <svg class="contact-icon" viewBox="0 0 26 26" aria-hidden="true">
          <circle cx="13" cy="13" r="12" fill="none" stroke="var(--gold)" stroke-width="1.5"/>
          <circle cx="13" cy="13" r="7" fill="none" stroke="var(--gold)" stroke-width="1.3"/>
          <ellipse cx="13" cy="13" rx="3" ry="7" fill="none" stroke="var(--gold)" stroke-width="1.1"/>
          <line x1="6" y1="13" x2="20" y2="13" stroke="var(--gold)" stroke-width="1.1"/>
          <line x1="7.5" y1="9.5" x2="18.5" y2="9.5" stroke="var(--gold)" stroke-width="1"/>
          <line x1="7.5" y1="16.5" x2="18.5" y2="16.5" stroke="var(--gold)" stroke-width="1"/>
        </svg>
        www.miriambaskell.example
      </span>
      <span class="contact-divider"></span>
      <span class="contact-item contact-item--mail">
        <svg class="contact-icon" viewBox="0 0 26 26" aria-hidden="true">
          <circle cx="13" cy="13" r="12" fill="none" stroke="var(--gold)" stroke-width="1.5"/>
          <rect x="6.5" y="8.5" width="13" height="9" fill="var(--gold)"/>
          <path d="M6.5 8.5 L13 13.5 L19.5 8.5" fill="none" stroke="#fff" stroke-width="1.2"/>
        </svg>
        miriam@miriambaskell.example
      </span>
    </div>
  </main>
</body>
</html>
```